Flyer für trilinguale Montessorischule
Zielgruppe
Wir sind eine trilinguale Montessorischule im Herzen der Natur und möchten einen neuen Flyer gestalten für unsere Zielgruppe (Eltern mit Kindern von3-12 Jahren)
Aufgabenstellung
Wichtig ist, dass die Angaben auf französisch und englisch angegegen werden - gerne ein 2-seitiger Flyer. Unser Logo, Design unseres Schulbusses etc. hänge ich unten an. Wichtig ist, in dem Rahmen zu arbeiten. Keywords sind auf dem Bus gut herausgearbeitet.
Wir sind eine familiäre Montessori Schule, die das Kind ins Zentrum setzt. We love what we do. Unsere qualitativ hochwertige Arbeit wird von gut ausgebildeten Lehrkräften liebevoll durchgeführt. Es gibt immer 2 Lehrkräfte in der Klasse (FR, EN und ab 6 Jahren auch noch deutsch dazu).
Details über die Schule:
We believe in teaching new skills in a child-centered way. We provide space for discovery and for opening up to others. Operated by parents and fueled by a strong sense of community our school provides highest quality Montessori education for children aged 3 to 12, a bilingual approach (English & French) for the younger age group, a trilingual approach (English, French and German) for the older age group, freshly-prepared meals, full-day care and free scheduled transportation.
Nous croyons en l'enseignement de nouvelles compétences de manière centrée sur l'enfant. Nous offrons un espace pour la découverte et pour s'ouvrir aux autres. Géré par des parents et alimenté par un fort sentiment de communauté, notre école propose une éducation Montessori de la plus grande qualité pour les enfants de 3 à 12 ans, une approche bilingue (anglais et français) pour le groupe d'âge le plus jeune, une approche trilingue (anglais, français et allemand) pour le groupe d'âge le plus âgé, des repas fraîchement préparés, une garde à temps plein et un service de transport gratuit.

```html
<!DOCTYPE html>
<html lang="fr">
<head>
<meta charset="utf-8">
<title>Ecole Montessori Trois Cent Racines – Flyer</title>
<link href="https://fonts.googleapis.com/css2?family=Open+Sans:wght@400;600;700&display=swap" rel="stylesheet">
<style>
  :root {
    --olive: #6f8c45;
    --leaf: #8fc23f;
    --lime: #c6d83a;
    --accent-text: #d7e23c;
    --paper: #fbfbf9;
    --ink: #3f3f3f;
    --stage: #e8e6e1;
    --photo-warm: #c98a3f;
    --photo-light: #e8b873;
    --photo-rose: #d9a6a8;
  }
  * { box-sizing: border-box; margin: 0; padding: 0; }
  html, body {
    width: 1200px; height: 900px; overflow: hidden;
    background: var(--stage);
    font-family: "Open Sans", Arial, sans-serif;
  }
  .flyer-side {
    position: absolute; left: 180px;
    width: 840px; height: 410px;
    background: var(--paper);
    overflow: hidden;
    box-shadow: 0 6px 18px rgba(0,0,0,.18);
  }
  .flyer-front { top: 30px; }
  .flyer-back { top: 460px; }
  .flyer-shapes { position: absolute; inset: 0; width: 840px; height: 410px; }

  .school-name {
    position: absolute; display: flex; align-items: center; gap: 12px;
    color: var(--olive); font-weight: 700; font-size: 21px; line-height: 1.15;
  }
  .school-name .name-dot {
    width: 40px; height: 40px; border-radius: 50%; background: var(--lime); flex: none;
  }
  .flyer-front .school-name { left: 52px; top: 150px; }
  .flyer-back .school-name { left: 238px; top: 296px; font-size: 17px; }
  .flyer-back .school-name .name-dot { width: 32px; height: 32px; }

  .web-line, .place-line {
    position: absolute; display: flex; align-items: center; gap: 8px;
    color: #fff; font-weight: 700;
  }
  .web-line { left: 396px; top: 22px; font-size: 15px; }
  .place-line { left: 660px; top: 62px; font-size: 14px; }
  .web-line svg, .place-line svg { flex: none; }

  .language-block {
    position: absolute; left: 348px; top: 150px; width: 200px;
    text-align: center; text-transform: uppercase; font-weight: 700;
  }
  .language-block .languages { color: #fff; font-size: 10.5px; letter-spacing: .2px; }
  .language-block .languages .sep { color: var(--accent-text); }
  .language-block .ages { color: var(--accent-text); font-size: 13px; margin: 3px 0 6px; }
  .language-block .rule { height: 1px; background: rgba(255,255,255,.8); margin: 0 0 8px; }

  .about-text {
    position: absolute; left: 400px; top: 34px; width: 414px;
    text-align: right; color: var(--ink); font-size: 11.2px; line-height: 1.38;
  }
  .about-text p + p { margin-top: 9px; }

  .contact-block {
    position: absolute; right: 28px; bottom: 14px;
    text-align: right; color: #fff; font-weight: 700; font-size: 13px; line-height: 1.4;
  }
</style>
</head>
<body>

<section class="flyer-side flyer-front">
  <svg class="flyer-shapes" viewBox="0 0 840 410" aria-hidden="false">
    <path d="M345,0 C385,150 335,320 285,410 L840,410 L840,0 Z" fill="var(--olive)"/>
    <path d="M560,0 L840,0 L840,162 Q740,170 652,200 C622,130 600,60 560,0 Z" fill="var(--leaf)"/>
    <path d="M430,410 C480,300 560,228 660,196 L840,160 L840,410 Z" fill="var(--lime)"/>
    <defs>
      <linearGradient id="photoTones" x1="0" y1="0" x2="1" y2="1">
        <stop offset="0" stop-color="var(--photo-warm)"/>
        <stop offset=".55" stop-color="var(--photo-light)"/>
        <stop offset="1" stop-color="var(--photo-rose)"/>
      </linearGradient>
    </defs>
    <path role="img" aria-label="Photo: smiling child working with Montessori material at a classroom table"
          d="M648,210 Q740,172 840,164 L840,410 L560,410 C590,330 612,262 648,210 Z"
          fill="url(#photoTones)"/>
  </svg>

  <div class="school-name"><span class="name-dot"></span><span>Ecole Montessori<br>Trois Cent Racines</span></div>

  <div class="web-line">
    <svg width="20" height="20" viewBox="0 0 20 20" fill="none" stroke="var(--lime)" stroke-width="1.5">
      <circle cx="10" cy="10" r="8"/><ellipse cx="10" cy="10" rx="3.5" ry="8"/><path d="M2 10h16M4 5.5h12M4 14.5h12"/>
    </svg>
    www.troiscentracines.ch
  </div>

  <div class="place-line">
    <svg width="16" height="20" viewBox="0 0 16 20">
      <path d="M8 0C3.6 0 0 3.5 0 7.8 0 13.4 8 20 8 20s8-6.6 8-12.2C16 3.5 12.4 0 8 0z" fill="var(--olive)"/>
      <circle cx="8" cy="7.6" r="3" fill="var(--leaf)"/>
    </svg>
    Les Vergers (Morges)
  </div>

  <div class="language-block">
    <div class="languages">English <span class="sep">•</span> French <span class="sep">•</span> German</div>
    <div class="ages">From 3 to 12 years</div>
    <div class="rule"></div>
    <div class="languages">Anglais <span class="sep">•</span> Français <span class="sep">•</span> Allemand</div>
    <div class="ages">De 3 à 12 ans</div>
    <div class="rule"></div>
  </div>
</section>

<section class="flyer-side flyer-back">
  <svg class="flyer-shapes" viewBox="0 0 840 410" aria-hidden="true">
    <path d="M0,0 L450,0 C350,60 280,170 250,410 L0,410 Z" fill="var(--leaf)"/>
    <path d="M0,0 L200,0 C255,120 250,270 185,410 L0,410 Z" fill="var(--olive)"/>
    <path d="M215,262 C260,200 310,160 372,128 C300,200 262,300 250,410 L185,410 C205,360 214,310 215,262 Z" fill="var(--lime)"/>
    <path d="M330,410 C430,330 610,312 840,318 L840,410 Z" fill="var(--olive)"/>
  </svg>

  <div class="about-text">
    <p>We believe in teaching new skills in a child-centered way. We provide space for discovery and for opening up to others. Operated by parents and fueled by a strong sense of community our school provides highest quality Montessori education for children aged 3 to 12, a bilingual approach (English &amp; French) for the younger age group, a trilingual approach (English, French and German) for the older age group, freshly-prepared meals, full-day care and free scheduled transportation.</p>
    <p>Nous croyons en l'enseignement de nouvelles compétences de manière centrée sur l'enfant. Nous offrons un espace pour la découverte et pour s'ouvrir aux autres. Géré par des parents et alimenté par un fort sentiment de communauté, notre école propose une éducation Montessori de la plus haute qualité pour les enfants de 3 à 12 ans, une approche bilingue (anglais et français) pour le groupe d'âge plus jeune, une approche trilingue (anglais, français et allemand) pour le groupe d'âge plus âgé, des repas fraîchement préparés, une garde à temps plein et un transport gratuit sur rendez-vous.</p>
  </div>

  <div class="school-name"><span class="name-dot"></span><span>Ecole Montessori<br>Trois Cent Racines</span></div>

  <div class="contact-block">
    fenwarilo@troiscentracines.ch<br>
    +41 76 412 58 93<br>
    www.troiscentracines.ch
  </div>
</section>

</body>
</html>
```